Bref créative
BrightPath Fuel
Eye Catching Card & Letterhead Design
Professional
Marcus Torres
CEO
4183 HAWTHORNE AVE
SUITE 310
SARASOTA FL 34519
mtorres@brightpathfuel.example
www.brightpathfuel.example
use the WELL portion of the logo and list the twitter site (@brightpathfuel)

```html
<!DOCTYPE html>
<html lang="en">
<head>
<meta charset="utf-8">
<title>BrightPath Fuel — Stationery Set</title>
<link href="https://fonts.googleapis.com/css2?family=Montserrat:wght@400;600;700&family=Open+Sans:wght@400;600&display=swap" rel="stylesheet">
<style>
  :root {
    --board: #ecebe7;
    --paper: #ffffff;
    --green: #8cc63f;
    --green-dark: #6a9e25;
    --green-soft: #dcebc4;
    --ink: #3a3a3a;
    --ink-light: #7a7a7a;
    --black: #1c1c1c;
    --shadow: 0 2px 6px rgba(0,0,0,.22);
  }
  * { box-sizing: border-box; margin: 0; padding: 0; }
  html, body { width: 1200px; height: 437px; overflow: hidden; }
  body {
    background: var(--board);
    font-family: "Open Sans", Arial, sans-serif;
    color: var(--ink);
    position: relative;
  }
  .piece { position: absolute; background: var(--paper); box-shadow: var(--shadow); overflow: hidden; }
  .wordmark {
    font-family: "Montserrat", Arial, sans-serif;
    font-weight: 700;
    color: var(--green-dark);
    text-transform: uppercase;
    letter-spacing: .5px;
    display: flex; align-items: center; gap: 4px;
    white-space: nowrap;
  }
  .wordmark .dot { width: 7px; height: 7px; border-radius: 50%; background: var(--green); flex: none; }
  .wave { position: absolute; left: 0; bottom: 0; width: 100%; }
  .caption {
    position: absolute; font-size: 7px; color: var(--ink-light);
    font-family: "Open Sans", Arial, sans-serif; white-space: nowrap;
  }
  .contact { font-size: 5.5px; line-height: 1.45; color: var(--ink); white-space: nowrap; }
  .contact strong { font-weight: 600; font-size: 6.5px; }

  /* business cards */
  .card { left: 24px; width: 190px; height: 98px; }
  .card--front { top: 92px; }
  .card--front .wordmark { position: absolute; left: 10px; top: 12px; font-size: 8px; }
  .card--front .wordmark .dot { width: 6px; height: 6px; }
  .card--front .contact { position: absolute; right: 10px; top: 28px; text-align: right; font-size: 5px; line-height: 1.4; }
  .card--front .contact strong { font-size: 6px; }
  .card--back { top: 204px; }
  .card--back .wordmark { position: absolute; left: 0; right: 0; top: 36px; justify-content: center; font-size: 9px; }
  .card--green { top: 316px; background: linear-gradient(160deg, var(--green) 0%, var(--green-dark) 100%); }
  .card--green .foliage {
    position: absolute; left: 50%; top: 10px; width: 70px; height: 70px; margin-left: -35px;
    border-radius: 50%;
    background: radial-gradient(circle, rgba(255,255,255,.55) 0%, rgba(255,255,255,0) 70%);
  }

  /* letterheads */
  .letterhead { top: 30px; width: 262px; height: 348px; }
  .letterhead--one { left: 240px; }
  .letterhead--two { left: 520px; }
  .letterhead .wordmark { position: absolute; left: 20px; top: 22px; font-size: 10px; }
  .letterhead .contact { position: absolute; left: 160px; top: 18px; }
  .letterhead .foliage {
    position: absolute; left: 56px; top: 110px; width: 150px; height: 150px; border-radius: 50%;
    background: radial-gradient(circle, var(--green-soft) 0%, rgba(220,235,196,0) 70%);
  }
  .letterhead .footer-web { position: absolute; right: 16px; bottom: 8px; font-size: 5.5px; color: #fff; }

  /* envelopes */
  .envelope { width: 390px; }
  .envelope--black { left: 790px; top: 22px; height: 104px; background: var(--black); }
  .envelope--green { left: 790px; top: 142px; height: 104px; }
  .envelope--back { left: 790px; top: 262px; height: 90px; }
  .envelope--front { left: 812px; top: 312px; height: 104px; }
  .flap { position: absolute; left: 0; top: 0; width: 100%; height: 60%; }
  .envelope--black .wordmark { position: absolute; left: 0; right: 0; top: 12px; justify-content: center; font-size: 9px; color: var(--green); }
  .envelope--green .wordmark { position: absolute; left: 0; right: 0; top: 10px; justify-content: center; font-size: 9px; }
  .envelope--front .wordmark { position: absolute; left: 14px; top: 12px; font-size: 10px; }
  .envelope--front .contact { position: absolute; right: 18px; bottom: 34px; text-align: right; }
</style>
</head>
<body>

<svg width="0" height="0" style="position:absolute">
  <defs>
    <symbol id="band" viewBox="0 0 100 30" preserveAspectRatio="none">
      <path d="M0 12 C30 2 60 22 100 8 L100 30 L0 30 Z" fill="#1c1c1c"/>
      <path d="M0 15 C30 6 60 25 100 12 L100 30 L0 30 Z" fill="#ffffff"/>
      <path d="M0 18 C30 10 60 27 100 15 L100 30 L0 30 Z" fill="#8cc63f"/>
    </symbol>
  </defs>
</svg>

<!-- Business cards -->
<section class="piece card card--front">
  <div class="wordmark"><span class="dot"></span>BrightPath Fuel</div>
  <div class="contact">
    <strong>Marcus Torres</strong><br>CEO<br>
    4183 HAWTHORNE AVE, SUITE 310<br>SARASOTA FL 34519<br>
    Ph. 941.555.0187<br>mtorres@brightpathfuel.example<br>@brightpathfuel
  </div>
  <svg class="wave" height="18"><use href="#band"/></svg>
</section>
<span class="caption" style="left:24px;top:192px">Business Card Front</span>

<section class="piece card card--back">
  <div class="wordmark"><span class="dot"></span>BrightPath Fuel</div>
  <svg class="wave" height="16"><use href="#band"/></svg>
</section>
<span class="caption" style="left:24px;top:304px">Business Card Back</span>

<section class="piece card card--green">
  <div class="foliage" role="img" aria-label="White leafy tree growing from the brand well"></div>
</section>
<span class="caption" style="left:24px;top:418px">Business Card Back 2</span>

<!-- Letterheads -->
<section class="piece letterhead letterhead--one">
  <div class="wordmark"><span class="dot"></span>BrightPath Fuel</div>
  <div class="contact">
    4183 HAWTHORNE AVE, SUITE 310<br>SARASOTA FL 34519<br>Ph. 941.555.0187<br>Fax 941.555.0188
  </div>
  <div class="foliage" role="img" aria-label="Faint leaf cluster decoration"></div>
  <svg class="wave" height="70"><use href="#band"/></svg>
  <span class="footer-web">www.brightpathfuel.example</span>
</section>
<span class="caption" style="left:240px;top:382px">Letterhead Page 1</span>

<section class="piece letterhead letterhead--two">
  <div class="wordmark"><span class="dot"></span>BrightPath Fuel</div>
  <div class="foliage" role="img" aria-label="Faint leaf cluster decoration"></div>
  <svg class="wave" height="70"><use href="#band"/></svg>
  <span class="footer-web">www.brightpathfuel.example</span>
</section>
<span class="caption" style="left:520px;top:382px">Letterhead Page 2</span>

<!-- Envelopes -->
<section class="piece envelope envelope--black">
  <svg class="flap" viewBox="0 0 100 60" preserveAspectRatio="none">
    <path d="M0 0 L50 55 L100 0" fill="none" stroke="#8cc63f" stroke-width=".6"/>
  </svg>
  <div class="wordmark"><span class="dot"></span>BrightPath Fuel</div>
</section>

<section class="piece envelope envelope--green">
  <svg class="flap" viewBox="0 0 100 60" preserveAspectRatio="none">
    <path d="M0 0 L50 55 L100 0 Z" fill="#8cc63f"/>
    <path d="M0 0 L50 55 L100 0" fill="none" stroke="#6a9e25" stroke-width=".6"/>
  </svg>
  <div class="wordmark" style="color:#fff"><span class="dot" style="background:#fff"></span>BrightPath Fuel</div>
</section>

<section class="piece envelope envelope--back">
  <svg class="flap" viewBox="0 0 100 60" preserveAspectRatio="none">
    <path d="M0 0 L50 55 L100 0" fill="none" stroke="#cfcfcf" stroke-width=".6"/>
  </svg>
</section>

<section class="piece envelope envelope--front">
  <div class="wordmark"><span class="dot"></span>BrightPath Fuel</div>
  <div class="contact">
    4183 HAWTHORNE AVE, SUITE 310<br>SARASOTA FL 34519<br>www.brightpathfuel.example
  </div>
  <svg class="wave" height="30"><use href="#band"/></svg>
</section>
<span class="caption" style="left:1060px;top:6px">Envelope Front &amp; Back</span>

</body>
</html>
```